Stationery Design Project - Ma clairiere

We are a french company, Ma Clairiere. It means My Glade.
We own and manage woods, we transform it industrially into very high quality (dry) logs and pellets and we commercialize them to individuals in France.
People can order the logs online or by phone and get the wood logs delivered at home.

After our great logo contest, we would like to launch a new stationery project.
Updates

Target Market(s)

inhabitants of sub-urban areas in France. (living in houses not in apartment )

Industry/Entity Type

It Company

Requirements
Must have
• content see attachment
logo

For the business card, we would like on the front side, the logo, name + contact info. We would like to use the back side for commercial purpose insisting on our distinctive value proposition.
Nice to have
• the back side of the business card can be more colorful

```html
<!DOCTYPE html>
<html lang="fr">
<head>
<meta charset="utf-8">
<title>Ma Clairiere – Carte de visite</title>
<link href="https://fonts.googleapis.com/css2?family=Arimo:wght@400;700&display=swap" rel="stylesheet">
<style>
  :root {
    --stage: #e6e4e1;
    --card: #ffffff;
    --ink: #2e2e2e;
    --ink-soft: #3c3c3c;
    --accent: #c4161c;
    --wood-light: #e9a64a;
    --wood-mid: #d98f2e;
    --wood-dark: #b8721c;
    --rule: #cfcfcf;
    --illus-shirt: #b3262b;
    --illus-skin: #c9a27e;
  }
  * { box-sizing: border-box; margin: 0; padding: 0; }
  html, body {
    width: 1200px; height: 775px; overflow: hidden;
    background: var(--stage);
    font-family: "Arimo", Arial, sans-serif;
  }
  .stage {
    position: relative; width: 1200px; height: 775px;
    display: flex; align-items: center; justify-content: center; gap: 40px;
  }
  .card {
    position: relative; width: 540px; height: 309px;
    box-shadow: 0 6px 18px rgba(0,0,0,.18);
    overflow: hidden;
  }

  /* Back side */
  .card--back { color: #fff; }
  .card__wood {
    position: absolute; inset: 0;
    background: linear-gradient(160deg, var(--wood-light) 0%, var(--wood-mid) 55%, var(--wood-dark) 100%);
  }
  .pitch {
    position: absolute; inset: 0;
    display: flex; flex-direction: column; align-items: center; justify-content: center;
    gap: 6px; text-align: center; padding: 0 30px;
    font-size: 14px; line-height: 1.35;
    text-shadow: 0 1px 2px rgba(0,0,0,.35);
  }
  .pitch__lead { font-size: 15px; }
  .pitch__gap { height: 14px; }

  /* Front side */
  .card--front { background: var(--card); color: var(--ink); }
  .mascot {
    position: absolute; left: 215px; top: 22px; width: 120px; height: 78px;
    background: linear-gradient(180deg, var(--illus-skin) 0%, var(--illus-shirt) 75%);
    border-radius: 6px;
  }
  .brand {
    position: absolute; left: 128px; top: 100px;
    font-size: 40px; font-weight: 700; letter-spacing: -1.5px;
    color: var(--ink-soft);
  }
  .divider {
    position: absolute; left: 272px; top: 168px; width: 1px; height: 100px;
    background: var(--rule);
  }
  .contact {
    position: absolute; right: 28px; top: 152px; text-align: right;
    font-size: 13px; line-height: 1.55;
  }
  .contact__name { font-size: 17px; font-weight: 700; margin-bottom: 6px; }
  .contact__line { display: flex; align-items: center; justify-content: flex-end; gap: 8px; }
  .contact__line svg { width: 12px; height: 12px; flex: none; }
  .contact__line--mail { margin-right: 20px; }
  .tagline {
    position: absolute; left: 40px; bottom: 34px;
    font-size: 14px; line-height: 1.4;
  }
  .tagline__url { color: var(--accent); }
</style>
</head>
<body>
<main class="stage">

  <section class="card card--back" aria-label="Verso de la carte">
    <div class="card__wood" role="img" aria-label="Motif de rondins de bois empilés"></div>
    <div class="pitch">
      <p class="pitch__lead">Livraison gratuite de bois de chauffage à Lyon et sa région</p>
      <p>Bûches, granulés, briquettes</p>
      <div class="pitch__gap"></div>
      <p>Commandez sur www.maclairiere.fr ou au 04 72 18 40 26</p>
      <p>Qualité supérieure, origine régionale certifiée, livraison en 48h</p>
    </div>
  </section>

  <section class="card card--front" aria-label="Recto de la carte">
    <div class="mascot" role="img" aria-label="Illustration d'un bûcheron en chemise à carreaux portant des bûches"></div>
    <div class="brand">Ma Clairiere</div>
    <div class="divider"></div>
    <div class="contact">
      <p class="contact__name">Jean-Luc MARTIN</p>
      <p class="contact__line">04 72 18 40 26
        <svg viewBox="0 0 12 12" aria-hidden="true"><rect x="3" y="0.5" width="6" height="11" rx="1" fill="none" stroke="var(--accent)" stroke-width="1.2"/></svg>
      </p>
      <p class="contact__line">04 72 18 40 26
        <svg viewBox="0 0 12 12" aria-hidden="true"><path d="M2 1.5 L4.2 1 L5.2 3.6 L3.8 4.6 Q5 7.2 7.4 8.2 L8.4 6.8 L11 7.8 L10.5 10 Q5 11 1.5 4 Z" fill="var(--accent)"/></svg>
      </p>
      <p class="contact__line contact__line--mail">martin@maclairiere.fr</p>
    </div>
    <div class="tagline">
      <p>Entre nous, ça chauffe !</p>
      <p class="tagline__url">www.maclairiere.fr</p>
    </div>
    <svg style="position:absolute;right:28px;top:225px;width:12px;height:12px" viewBox="0 0 12 12" aria-hidden="true"><rect x="0.5" y="2" width="11" height="8" fill="var(--accent)"/><path d="M0.5 2 L6 6.5 L11.5 2" fill="none" stroke="#fff" stroke-width="1"/></svg>
  </section>

</main>
</body>
</html>
```